Business Card Designs

Looking to design a 3.5" x 2" standard business card for our employees.
The design needs to be sleek, simple, and modern. We would like our logo (attached) to be incorporated, but not in that colour, rather an outline of the logo in either gold or silver (whichever looks better).

Modern and Simple is what we are looking for, but be creative in incorporating the logo.

```html
<!DOCTYPE html>
<html lang="en">
<head>
<meta charset="utf-8">
<title>Harbourline Suites – Business Card</title>
<link rel="stylesheet" href="https://fonts.googleapis.com/css2?family=Montserrat:wght@400;500;700&display=swap">
<style>
  :root {
    --teal: #62a3a0;
    --teal-dark: #4f8f8c;
    --white: #ffffff;
    --rule: #a9a9a9;
    --stage: #2b2b2b;
  }
  * { box-sizing: border-box; margin: 0; padding: 0; }
  html, body { width: 1200px; height: 960px; overflow: hidden; }
  body {
    background: var(--stage);
    font-family: "Montserrat", sans-serif;
    position: relative;
  }
  .card {
    position: absolute;
    left: 250px;
    width: 700px;
    height: 400px;
    border-radius: 22px;
    overflow: hidden;
    box-shadow: 0 10px 28px rgba(0,0,0,.45);
  }
  .card--front { top: 50px; background: var(--teal); }
  .card--back  { top: 500px; background: var(--white); }

  .wordmark {
    display: flex;
    align-items: center;
    gap: 14px;
    font-weight: 500;
    letter-spacing: .22em;
    text-transform: uppercase;
  }
  .wordmark__square { width: 16px; height: 16px; }

  .card--front .wordmark {
    position: absolute; inset: 0;
    justify-content: center;
    color: var(--white);
    font-size: 30px;
  }
  .card--front .wordmark__square { background: var(--white); width: 22px; height: 22px; }

  .back__top {
    position: absolute; left: 0; top: 0; width: 100%; height: 210px;
    display: flex; align-items: center; justify-content: center;
  }
  .card--back .wordmark { color: var(--teal); font-size: 22px; }
  .card--back .wordmark__square { background: var(--teal); }

  .back__rule {
    position: absolute; left: 0; top: 210px; width: 100%; height: 6px;
    background: var(--rule);
  }
  .back__band {
    position: absolute; left: 0; top: 216px; width: 100%; height: 184px;
    background: var(--teal);
    color: var(--white);
  }
  .person {
    position: absolute; left: 40px; top: 58px;
    padding-left: 16px;
    border-left: 6px solid var(--white);
  }
  .person__name { font-size: 26px; font-weight: 700; letter-spacing: .01em; line-height: 1.1; }
  .person__title { font-size: 17px; font-weight: 400; margin-top: 4px; }

  .contact {
    position: absolute; right: 36px; top: 20px;
    list-style: none;
    font-size: 16px;
    line-height: 1.45;
  }
  .contact__address { margin-bottom: 6px; }
  .contact__item { display: flex; align-items: center; gap: 10px; }
  .contact__icon { width: 16px; height: 16px; flex: none; }
</style>
</head>
<body>

  <section class="card card--front" aria-label="Card front">
    <div class="wordmark">
      <span class="wordmark__square"></span>
      <span>Harbourline Suites</span>
    </div>
  </section>

  <section class="card card--back" aria-label="Card back">
    <div class="back__top">
      <div class="wordmark">
        <span class="wordmark__square"></span>
        <span>Harbourline Suites</span>
      </div>
    </div>
    <div class="back__rule"></div>
    <div class="back__band">
      <div class="person">
        <p class="person__name">DARA WHITFIELD</p>
        <p class="person__title">Managing Director</p>
      </div>
      <ul class="contact">
        <li class="contact__address">1180 Maple Crest Avenue<br>Ottawa, ON, K1P 4T7</li>
        <li class="contact__item">
          <svg class="contact__icon" viewBox="0 0 16 16" aria-hidden="true"><path fill="#fff" d="M3 1.5l2.5 0 1 3.5-1.6 1.2a8 8 0 0 0 4.9 4.9L11 9.5l3.5 1v2.5c0 .8-.7 1.5-1.5 1.5A12 12 0 0 1 1.5 3c0-.8.7-1.5 1.5-1.5z"/></svg>
          <span>555-204-3187</span>
        </li>
        <li class="contact__item">
          <svg class="contact__icon" viewBox="0 0 16 16" aria-hidden="true"><rect x="1" y="3" width="14" height="10" fill="#fff"/><path d="M1 3l7 6 7-6" fill="none" stroke="#62a3a0" stroke-width="1.4"/></svg>
          <span>hello@harbourlinesuites.com</span>
        </li>
        <li class="contact__item">
          <svg class="contact__icon" viewBox="0 0 16 16" aria-hidden="true"><circle cx="8" cy="8" r="7" fill="#fff"/><path d="M1 8h14M8 1c-3 3.5-3 10.5 0 14M8 1c3 3.5 3 10.5 0 14" fill="none" stroke="#62a3a0" stroke-width="1"/></svg>
          <span>www.harbourlinesuites.com</span>
        </li>
      </ul>
    </div>
  </section>

</body>
</html>
```